Business Card Design using new attached logo

We are a family run Plumbing and Heating firm looking to improve our company image with an improved business card and new logo.We are looking to keep the company colour (Blue) involved in our design

Reason: New logo added which needs to be incorporated on designs

Industry/Entity Type

Business

Contact Information for Business Card

See attachment of all info required.

Requirements
Must have
• We have just picked a new company logo which is attached.
• Could you please provide your business card designs using this logo.
• We are looking for the logo on the back as well as the front with all the info required

```html
<!DOCTYPE html>
<html lang="en">
<head>
<meta charset="utf-8">
<title>Halden Heating Ltd – Business Cards</title>
<link rel="stylesheet" href="https://fonts.googleapis.com/css2?family=Libre+Baskerville:ital,wght@0,400;0,700;1,700&display=swap">
<style>
  :root {
    --bg: #1b1b1b;
    --brand-blue: #0a3a70;
    --card-white: #ffffff;
    --ink: #1e1e1e;
  }
  * { margin: 0; padding: 0; box-sizing: border-box; }
  html, body {
    width: 1200px; height: 1000px; overflow: hidden;
    background: var(--bg);
    font-family: "Libre Baskerville", "Times New Roman", serif;
  }
  .stage { position: relative; width: 1200px; height: 1000px; }
  .card {
    position: absolute; width: 600px; height: 340px; overflow: hidden;
  }
  .card-back {
    left: 530px; top: 110px;
    background: var(--brand-blue);
    display: flex; align-items: center; justify-content: center;
  }
  .card-back .brand-name {
    color: var(--card-white);
    font-size: 44px; font-weight: 700; letter-spacing: 0.5px;
  }
  .card-front {
    left: 70px; top: 560px;
    background: var(--card-white);
    color: var(--ink);
  }
  .card-front .brand-name {
    position: absolute; left: 300px; top: 62px;
    color: var(--brand-blue);
    font-size: 24px; font-weight: 700;
  }
  .holder {
    position: absolute; left: 30px; top: 150px;
    color: var(--brand-blue);
  }
  .holder-name { font-size: 17px; font-weight: 700; letter-spacing: 0.5px; }
  .holder-role { font-size: 11px; font-weight: 700; font-style: italic; }
  .contact {
    position: absolute; left: 258px; top: 168px;
    font-size: 13px; font-weight: 700; line-height: 1.45;
  }
  .address { text-transform: uppercase; margin-left: 14px; margin-bottom: 12px; }
  .phones { margin-bottom: 14px; }
  .email { font-weight: 400; }
  .base-band {
    position: absolute; left: 270px; right: 0; bottom: 0; height: 18px;
    background: var(--brand-blue);
  }
</style>
</head>
<body>
  <main class="stage">
    <section class="card card-back" aria-label="Card back">
      <p class="brand-name">Halden Heating Ltd</p>
    </section>

    <section class="card card-front" aria-label="Card front">
      <p class="brand-name">Halden Heating Ltd</p>
      <div class="holder">
        <p class="holder-name">MARK ELLISON</p>
        <p class="holder-role">Director</p>
      </div>
      <div class="contact">
        <p class="address">14 Mill Parade, Fenwick Road<br>Ashford, Kent TN9 2QX</p>
        <p class="phones">T : 020 7946 0123<br>F : 020 7946 0456<br>M : 07700 900321</p>
        <p class="email">e : markellison@haldenheating.co.uk</p>
      </div>
      <div class="base-band"></div>
    </section>
  </main>
</body>
</html>
```